Micro Brewery Needs Generic Box Design

We need packaging artwork design for a beer box for small brewery located in the Kingdom of Tonga. We currently have two separate boxes for our flagship brands 'Tidecrest' & 'Melahu' (Tongan for Tidecrest).
The brewery is named 'The Tidecrest Brewery'. With premium new value add products using locally grown Vanilla, Ginger & Mango coming soon we require a generic box that can represent our Brewery and Tonga while reducing the costs involved in having artwork for each product line.
I have loaded files of our current box images. Please feel free to adapt from these or discard altogether.
All our products will be produced at 5% Alc/Vol and will contain 24 Bottles per box so these items should remain in the design layout.
Brewery

```html
<!DOCTYPE html>
<html lang="en">
<head>
<meta charset="utf-8">
<title>The Tidecrest Brewery – 24 Bottle Carton</title>
<link rel="stylesheet" href="https://fonts.googleapis.com/css2?family=Crimson+Text:wght@400;600&family=Montserrat:wght@500;700;800&display=swap">
<style>
  :root {
    --kraft: #c49a6b;
    --ink: #5e4a2e;
    --paper: #ffffff;
    --cut: #3a2e22;
    --fold: #d0463a;
    --art-light: #b48d62;
    --art-dark: #7d6341;
  }
  * { margin: 0; padding: 0; box-sizing: border-box; }
  html, body { width: 1200px; height: 600px; overflow: hidden; background: var(--paper); }
  .carton { position: relative; width: 1200px; height: 600px; }
  .dieline { position: absolute; inset: 0; }
  .serif { font-family: "Crimson Text", Georgia, serif; }
  .sans { font-family: "Montserrat", Arial, sans-serif; }

  .count { position: absolute; color: var(--paper); font-family: "Montserrat", Arial, sans-serif; text-align: center; line-height: 1; }
  .count .num { font-weight: 800; display: block; }
  .count .unit { font-weight: 700; display: block; letter-spacing: .5px; }
  .count .vol { font-weight: 500; display: block; }
  .count--large .num { font-size: 34px; }
  .count--large .unit { font-size: 9px; }
  .count--large .vol { font-size: 7px; }
  .count--small .num { font-size: 22px; }
  .count--small .unit { font-size: 6px; }
  .count--small .vol { font-size: 5px; }

  .alc { position: absolute; color: var(--paper); font-family: "Montserrat", Arial, sans-serif; font-weight: 800; line-height: 1; text-align: center; }
  .alc .pct { font-size: 17px; display: block; }
  .alc .lbl { font-size: 10px; display: block; }

  .options-row { position: absolute; display: flex; gap: 10px; color: var(--ink); font-size: 15px; white-space: nowrap; }
  .options-col { position: absolute; display: flex; flex-direction: column; gap: 6px; color: var(--ink); font-size: 15px; line-height: 1.05; }
  .option { display: flex; align-items: flex-start; gap: 4px; }
  .box { width: 11px; height: 11px; border: 1.4px solid var(--paper); background: transparent; margin-top: 3px; flex: none; }

  .origin { position: absolute; color: var(--ink); font-family: "Montserrat", Arial, sans-serif; font-weight: 500; letter-spacing: 2.5px; font-size: 10px; }
  .origin--stack { font-size: 11px; letter-spacing: 2.5px; line-height: 1.3; }

  .brand-name { position: absolute; color: var(--ink); font-family: "Crimson Text", Georgia, serif; font-weight: 600; text-align: center; line-height: 1; }
  .brand-name--front { font-size: 36px; width: 300px; }
  .brand-name--side { font-size: 16px; width: 110px; }
  .brand-name--flap { font-size: 30px; width: 300px; letter-spacing: 1px; }

  .artwork { position: absolute; background: radial-gradient(ellipse at 55% 45%, var(--art-light), var(--art-dark)); border-radius: 6px; opacity: .75; }
</style>
</head>
<body>
<main class="carton">
  <svg class="dieline" width="1200" height="600" viewBox="0 0 1200 600" aria-hidden="true">
    <rect x="38" y="12" width="1148" height="577" fill="var(--kraft)"/>
    <g fill="none" stroke="var(--cut)" stroke-width="1">
      <path d="M42 187 L55 72 L370 72 L381 187"/>
      <path d="M381 187 L398 18 L592 18 L609 187"/>
      <path d="M609 187 L622 72 L937 72 L947 187"/>
      <path d="M947 187 L964 18 L1150 18 L1165 187 L1165 412 L1150 580 L964 580 L947 412"/>
      <path d="M42 412 L55 528 L370 528 L381 412"/>
      <path d="M381 412 L398 580 L592 580 L609 412"/>
      <path d="M609 412 L622 528 L937 528 L947 412"/>
      <path d="M42 187 L30 187 Q25 187 25 192 L25 407 Q25 412 30 412 L42 412 Z"/>
      <path d="M42 187 L42 412"/>
    </g>
    <g fill="none" stroke="var(--fold)" stroke-width=".8" stroke-dasharray="3 2">
      <path d="M42 187 H1165 M42 412 H1165 M381 187 V412 M609 187 V412 M947 187 V412"/>
    </g>
  </svg>

  <!-- Front panel -->
  <div class="count count--large" style="left:190px;top:105px;"><span class="num">24</span><span class="unit">BOTTLES</span><span class="vol">330ml</span></div>
  <div class="options-row serif" style="left:96px;top:202px;">
    <span class="option"><span class="box"></span>Tidecrest</span>
    <span class="option"><span class="box"></span>Melahu</span>
    <span class="option"><span class="box"></span>Sparkling Water</span>
  </div>
  <div class="brand-name brand-name--front" style="left:62px;top:282px;">The Tidecrest Brewery</div>
  <div class="alc" style="left:60px;top:371px;"><span class="pct">5%</span><span class="lbl">ALC</span></div>
  <div class="origin" style="left:164px;top:384px;">MADE IN TONGA</div>
  <div class="count count--small" style="left:336px;top:370px;"><span class="num">24</span><span class="unit">BOTTLES</span><span class="vol">330ml</span></div>

  <!-- Side panel -->
  <div class="count count--small" style="left:396px;top:205px;"><span class="num">24</span><span class="unit">BOTTLES</span><span class="vol">330ml</span></div>
  <div class="brand-name brand-name--side" style="left:485px;top:213px;">The Tidecrest Brewery</div>
  <div class="options-col serif" style="left:397px;top:261px;">
    <span class="option"><span class="box"></span>Tidecrest</span>
    <span class="option"><span class="box"></span>Melahu</span>
    <span class="option"><span class="box"></span>Sparkling<br>Water</span>
  </div>
  <div class="origin origin--stack" style="left:395px;top:381px;">MADE IN<br>TONGA</div>
  <div class="artwork" role="img" aria-label="Engraved illustration of a brewer raising a glass of beer beside a barrel and hops" style="left:474px;top:258px;width:130px;height:152px;"></div>

  <!-- Back panel -->
  <div class="brand-name brand-name--flap" style="left:630px;top:100px;">The Tidecrest<br>BREWERY</div>
  <div class="options-row serif" style="left:663px;top:202px;">
    <span class="option"><span class="box"></span>Tidecrest</span>
    <span class="option"><span class="box"></span>Melahu</span>
    <span class="option"><span class="box"></span>Sparkling Water</span>
  </div>
  <div class="brand-name brand-name--front" style="left:629px;top:282px;">The Tidecrest Brewery</div>
  <div class="alc" style="left:627px;top:371px;"><span class="pct">5%</span><span class="lbl">ALC</span></div>
  <div class="origin" style="left:731px;top:384px;">MADE IN TONGA</div>
  <div class="count count--small" style="left:903px;top:370px;"><span class="num">24</span><span class="unit">BOTTLES</span><span class="vol">330ml</span></div>

  <!-- Second side panel -->
  <div class="count count--small" style="left:962px;top:205px;"><span class="num">24</span><span class="unit">BOTTLES</span><span class="vol">330ml</span></div>
  <div class="brand-name brand-name--side" style="left:1051px;top:213px;">The Tidecrest Brewery</div>
  <div class="options-col serif" style="left:963px;top:261px;">
    <span class="option"><span class="box"></span>Tidecrest</span>
    <span class="option"><span class="box"></span>Melahu</span>
    <span class="option"><span class="box"></span>Sparkling<br>Water</span>
  </div>
  <div class="origin origin--stack" style="left:962px;top:381px;">MADE IN<br>TONGA</div>
  <div class="artwork" role="img" aria-label="Engraved illustration of a brewer raising a glass of beer beside a barrel and hops" style="left:1040px;top:258px;width:125px;height:152px;"></div>
</main>
</body>
</html>
```